Flyer Design Project

We are offering a new class on cyber crime and want to advertise this course to students. We would like to see a design that is eye catching and coveys the goals of the course, when it meets and a brief abstract for the class.

The course will focus on the economics of cyber crime so including one or two graphics that get across this point would be good.

Requirements
Must have
• Course name "Cyber Crime"
Call number "CS 795 - 004"
Course meeting time (day of week and time) Tue. 4:30-7:10pm
Course goals
Course abstract

```html
<!DOCTYPE html>
<html lang="en">
<head>
<meta charset="utf-8">
<title>Cyber Smart about Cyber Crime – Course Flyer</title>
<link rel="stylesheet" href="https://fonts.googleapis.com/css2?family=Architects+Daughter&family=Black+Ops+One&family=Mulish:ital,wght@0,400;0,700;0,800;1,400;1,700&display=swap">
<style>
  :root {
    --paper: #d8d8d8;
    --paper-light: #e6e6e6;
    --ink: #111111;
    --alert-red: #e0201b;
    --tape-yellow: #f7f01a;
    --key-teal: #a9dfe0;
    --key-ink: #2e5656;
    --goal-teal: #a8e4e5;
    --lens-dark: #253a3b;
    --lens-mid: #5f9c9c;
    --lens-light: #a6d4d2;
    --photo-light: #f4f4f4;
    --photo-mid: #cfcfcf;
    --screen: #d9dcdc;
  }
  * { margin: 0; padding: 0; box-sizing: border-box; }
  html, body { width: 900px; height: 1200px; overflow: hidden; }
  body { background: var(--paper); font-family: "Mulish", "Century Gothic", sans-serif; color: var(--ink); }

  .flyer {
    position: relative; width: 900px; height: 1200px; overflow: hidden;
    background: linear-gradient(180deg, var(--paper-light) 0%, var(--paper) 40%, var(--paper) 100%);
  }

  .headline {
    position: absolute; left: 24px; top: 18px; white-space: nowrap; z-index: 3;
    font-family: "Architects Daughter", cursive; font-size: 50px; line-height: 1;
  }
  .headline .about { font-size: 34px; }
  .headline .stamp { font-family: "Black Ops One", sans-serif; font-size: 48px; letter-spacing: 1px; }

  .tagline {
    position: absolute; left: 30px; top: 110px; width: 290px; z-index: 3;
    font-size: 24px; line-height: 1.2; text-align: center;
  }
  .tagline .new { color: var(--alert-red); font-weight: 800; }

  .hero-lens { position: absolute; left: 150px; top: 76px; width: 740px; height: 624px; }

  .crime-tape {
    position: absolute; left: 264px; top: 249px; width: 640px; height: 58px;
    background: var(--tape-yellow); border: 3px solid var(--ink);
    transform: rotate(27deg); transform-origin: center;
    display: flex; align-items: center; justify-content: center;
    font-family: "Black Ops One", sans-serif; font-size: 24px; letter-spacing: 2px; white-space: nowrap;
  }

  .schedule-key {
    position: absolute; left: 258px; top: 446px; width: 340px; height: 110px;
    background: var(--key-teal); transform: rotate(20deg);
    color: var(--key-ink); text-align: center; padding-top: 14px;
  }
  .schedule-key .course-name { font-family: "Black Ops One", sans-serif; font-size: 36px; line-height: 1; }
  .schedule-key .meeting { font-size: 24px; margin-top: 8px; }

  .student-photo { position: absolute; left: 0; top: 528px; width: 412px; height: 596px; }

  .phone-screen {
    position: absolute; left: 58px; top: 702px; width: 88px; height: 170px;
    background: var(--screen); border-radius: 6px;
    font-weight: 800; font-size: 22px; line-height: 1.25; padding: 14px 0 0 12px;
  }

  .lead {
    position: absolute; left: 402px; top: 716px; width: 410px;
    font-style: italic; font-weight: 700; font-size: 21px; line-height: 1.22;
  }

  .counter {
    position: absolute; left: 448px; top: 808px;
    font-family: "Black Ops One", sans-serif; font-size: 34px; letter-spacing: 1px; line-height: 1;
  }

  .abstract {
    position: absolute; left: 402px; top: 852px; width: 430px;
    font-weight: 700; font-size: 17.5px; line-height: 24px;
  }
  .abstract .term { display: block; text-align: center; }

  .goal {
    position: absolute; background: var(--goal-teal);
    font-style: italic; font-size: 18.5px; line-height: 1.2; padding: 5px 12px;
  }
  .goal .arrow { font-style: normal; font-size: 13px; margin-right: 16px; vertical-align: 2px; }
  .goal.mechanics { left: 356px; top: 1044px; width: 542px; height: 52px; text-align: center; }
  .goal.intervention { left: 35px; top: 1114px; width: 540px; height: 52px; }
  .goal.intervention .first { display: block; padding-left: 38px; }
</style>
</head>
<body>
<main class="flyer">
  <svg class="hero-lens" viewBox="0 0 740 624" role="img" aria-label="Close-up photo of a keyboard with a dollar-sign card standing between the keys">
    <defs>
      <radialGradient id="lensFill" cx="45%" cy="45%" r="60%">
        <stop offset="0" stop-color="var(--lens-light)"/>
        <stop offset="0.55" stop-color="var(--lens-mid)"/>
        <stop offset="1" stop-color="var(--lens-dark)"/>
      </radialGradient>
    </defs>
    <ellipse cx="370" cy="312" rx="366" ry="308" fill="url(#lensFill)" stroke="var(--ink)" stroke-width="4"/>
  </svg>

  <h1 class="headline">Cyber Smart <span class="about">about</span> <span class="stamp">CYBER CRIME?</span></h1>
  <p class="tagline">A <span class="new">NEW</span> course about Cyber Crime</p>

  <div class="crime-tape">PROFIT-DRIVEN ECONOMIC CRIME SCENE</div>

  <div class="schedule-key">
    <div class="course-name">CYBER CRIME</div>
    <div class="meeting">Tuesdays – 4:30 pm-7:10 pm</div>
  </div>

  <svg class="student-photo" viewBox="0 0 412 596" role="img" aria-label="Photo of a smiling student holding out a mobile phone">
    <defs>
      <linearGradient id="photoFill" x1="0" y1="0" x2="1" y2="1">
        <stop offset="0" stop-color="var(--photo-light)"/>
        <stop offset="1" stop-color="var(--photo-mid)"/>
      </linearGradient>
    </defs>
    <rect width="412" height="596" fill="url(#photoFill)"/>
  </svg>

  <div class="phone-screen">Call:<br>CS<br>795<br>004</div>

  <p class="lead">The cyber-security landscape has exploded with a rise of profit-fueled cyber crime...</p>
  <h2 class="counter">COUNTER ATTACK?</h2>
  <p class="abstract">Obtaining a structural understanding of the underlying economics and associated business practices that lead to profit-driven cyber crime can illuminate new defensive measures. &nbsp;Come and research our current understanding of the economics of <span class="term">CYBER CRIME.</span></p>

  <p class="goal mechanics"><span class="arrow">➤</span>Understand how modern cyber crime<br>operates on a technical and economic level</p>
  <p class="goal intervention"><span class="first"><span class="arrow">➤</span>Analyze some of the potential places to</span>intervene at an economic, technical and policy level</p>
</main>
</body>
</html>
```